Easter & Summer School Dance Camps

I need two flyers one for Easter camps and one for summer school
We are a performing arts and dance academy

I want a double sided flyers one side summer school one side easter camp

Please make these flyers appeal to young dancers and performers - eye catching up to date Added Tuesday, March 1, 2016

Target Market(s)

Young children and teenagers

Industry/Entity Type

School

Font styles to use
Serif
Sans Serif

Requirements
Must have
• bright colourful

```html
<!DOCTYPE html>
<html lang="en">
<head>
<meta charset="utf-8">
<title>Brightstep Summer School Flyers</title>
<link rel="stylesheet" href="https://fonts.googleapis.com/css2?family=Oswald:wght@700&family=Cabin:wght@400;600&display=swap">
<style>
  :root {
    --canvas: #ececec;
    --ink-dark: #2b2b2b;
    --paper-light: #f7f7f7;
    --blue: #1f7fc6;
    --orange: #ee6135;
    --yellow: #f4be4c;
    --gold: #dfb43a;
    --pink: #f36fb1;
    --green: #6cc35a;
    --white: #ffffff;
    --black: #1b1b1b;
  }
  * { margin: 0; padding: 0; box-sizing: border-box; }
  html, body { width: 1200px; height: 900px; overflow: hidden; }
  body {
    background: var(--canvas);
    font-family: "Cabin", Arial, sans-serif;
    position: relative;
  }
  .flyer {
    position: absolute;
    top: 100px;
    width: 520px;
    height: 700px;
    overflow: hidden;
    box-shadow: 0 12px 30px rgba(0,0,0,0.18);
  }
  .flyer--dark { left: 50px; background: var(--ink-dark); color: var(--white); }
  .flyer--light { left: 630px; background: var(--paper-light); color: var(--black); }
  .flyer__shapes { position: absolute; inset: 0; width: 520px; height: 700px; }

  .flyer__title {
    position: absolute; left: 28px; top: 22px;
    font-family: "Oswald", Impact, sans-serif;
    font-weight: 700; font-size: 54px; line-height: 1.02;
    text-transform: uppercase; letter-spacing: 0.5px;
  }
  .flyer--dark .flyer__title { color: var(--white); }
  .flyer--light .flyer__title { color: var(--blue); }

  .flyer__intro {
    position: absolute; left: 28px; top: 212px; width: 262px;
    font-size: 11px; line-height: 1.3;
  }
  .flyer--dark .flyer__intro { color: #e6e6e6; }
  .flyer--light .flyer__intro { color: #333; }

  .venue {
    position: absolute; right: 32px; top: 256px; width: 130px;
    text-align: right; color: var(--white); font-size: 13.5px; line-height: 1.28;
  }
  .venue__label { font-weight: 600; font-size: 15px; margin-bottom: 3px; }

  .price {
    position: absolute; left: 340px; top: 432px; width: 100px;
    text-align: center; color: var(--white); font-size: 14px; line-height: 1.05;
  }
  .price__figure { font-weight: 600; font-size: 15px; }
  .price__divider { border-top: 1px dashed rgba(255,255,255,0.85); width: 56px; margin: 4px auto; }

  .workshop {
    position: absolute; left: 280px; top: 564px; width: 200px;
    text-align: center; color: var(--black);
  }
  .workshop__brand {
    display: inline-flex; align-items: center; gap: 6px;
    font-size: 26px; font-weight: 400; line-height: 1.2; margin-bottom: 8px;
  }
  .workshop__brand-dot { width: 11px; height: 11px; border-radius: 50%; background: var(--pink); }
  .workshop__details { font-size: 11.5px; line-height: 1.3; font-weight: 600; }

  .booking {
    position: absolute; left: 14px; top: 620px; color: var(--black); font-size: 13px;
  }
  .booking__label { font-weight: 600; font-size: 14px; }
  .booking__phone { display: flex; align-items: center; gap: 4px; font-weight: 600; font-size: 19px; }
  .booking__email { display: flex; align-items: center; gap: 4px; font-size: 11.5px; }
  .booking svg { flex: none; }
</style>
</head>
<body>

<article class="flyer flyer--dark">
  <svg class="flyer__shapes" viewBox="0 0 520 700">
    <polygon points="440,110 520,110 520,190" fill="var(--green)"/>
    <polygon points="520,150 520,250 470,250" fill="var(--pink)"/>
    <rect role="img" aria-label="White silhouette of a dancing girl" x="330" y="130" width="130" height="400" rx="65" fill="var(--white)"/>
    <polygon points="300,250 520,215 470,480" fill="var(--blue)" stroke="var(--ink-dark)" stroke-width="4"/>
    <polygon points="390,360 480,535 300,535" fill="var(--orange)" stroke="var(--ink-dark)" stroke-width="4"/>
    <polygon points="0,500 110,600 0,600" fill="var(--pink)"/>
    <polygon points="150,560 240,560 200,650" fill="var(--green)"/>
    <polygon points="250,600 390,700 200,700" fill="var(--pink)"/>
    <polygon points="0,600 190,600 235,700 0,700" fill="var(--yellow)"/>
    <rect role="img" aria-label="Blue silhouette of a boy dancing and pointing" x="175" y="450" width="120" height="250" rx="55" fill="var(--blue)"/>
    <polygon points="430,650 520,600 520,700" fill="var(--green)"/>
    <polygon points="520,560 520,640 470,640" fill="var(--orange)"/>
    <polygon points="230,545 530,545 380,760" fill="var(--yellow)" stroke="var(--ink-dark)" stroke-width="5"/>
    <polygon points="252,558 508,558 380,742" fill="none" stroke="var(--black)" stroke-width="1"/>
  </svg>

  <h1 class="flyer__title">Brightstep<br>Summer<br>School</h1>
  <p class="flyer__intro">Summer school is designed for young people who enjoy performing. The course introduces you to various disciplines of theatre: Acting, Singing and Dance. Everyone is able to develop at their own pace, no-one is forced to perform and there are opportunities for you to explore performance techniques. Students will develop key skills in teamwork, communication and confidence whilst building friendships and having fun! The week ends with a showing, to friends and family, of the skills and musical numbers achieved during the course.</p>

  <div class="venue">
    <div class="venue__label">VENUE</div>
    The Village Hall<br>of St Aldric<br>Riverside<br>KT0 1AA
  </div>

  <div class="price">
    <div class="price__figure">30</div>per day
    <div class="price__divider"></div>
    <div class="price__figure">55</div>for both
  </div>

  <div class="workshop">
    <div class="workshop__brand"><span class="workshop__brand-dot"></span>Brightstep</div>
    <div class="workshop__details">WEST END WORKSHOP<br>Tuesday<br>5 &amp; 6 April 2016<br>8 – 16 years<br>1-4pm</div>
  </div>

  <div class="booking">
    <div class="booking__label">FOR BOOKING</div>
    <div class="booking__phone"><svg width="10" height="16" viewBox="0 0 10 16"><rect x="1" y="1" width="8" height="14" rx="1.5" fill="none" stroke="var(--blue)" stroke-width="1.6"/></svg>07700 900123</div>
    <div class="booking__email"><svg width="11" height="8" viewBox="0 0 11 8"><rect width="11" height="8" fill="var(--blue)"/><polyline points="0,0 5.5,4.5 11,0" fill="none" stroke="var(--white)" stroke-width="1"/></svg>brightstepdance@mail.com</div>
  </div>
</article>

<article class="flyer flyer--light">
  <svg class="flyer__shapes" viewBox="0 0 520 700">
    <polygon points="440,0 520,0 520,70" fill="var(--green)"/>
    <polygon points="520,80 520,200 470,200" fill="var(--pink)"/>
    <rect role="img" aria-label="Gold silhouette of a dancing girl" x="330" y="60" width="130" height="470" rx="65" fill="var(--gold)"/>
    <polygon points="300,250 520,215 470,480" fill="var(--blue)" stroke="var(--paper-light)" stroke-width="4"/>
    <polygon points="390,360 480,535 300,535" fill="var(--orange)" stroke="var(--paper-light)" stroke-width="4"/>
    <polygon points="0,500 110,600 0,600" fill="var(--pink)"/>
    <polygon points="150,560 240,560 200,650" fill="var(--green)"/>
    <polygon points="250,600 390,700 200,700" fill="var(--pink)"/>
    <polygon points="0,600 190,600 235,700 0,700" fill="var(--yellow)"/>
    <rect role="img" aria-label="Blue silhouette of a boy dancing and pointing" x="175" y="450" width="120" height="250" rx="55" fill="var(--blue)"/>
    <polygon points="430,650 520,600 520,700" fill="var(--green)"/>
    <polygon points="520,560 520,640 470,640" fill="var(--orange)"/>
    <polygon points="230,545 530,545 380,760" fill="var(--yellow)" stroke="var(--paper-light)" stroke-width="5"/>
    <polygon points="252,558 508,558 380,742" fill="none" stroke="var(--black)" stroke-width="1"/>
  </svg>

  <h1 class="flyer__title">Brightstep<br>Summer<br>School</h1>
  <p class="flyer__intro">Summer school is designed for young people who enjoy performing. The course introduces you to various disciplines of theatre: Acting, Singing and Dance. Everyone is able to develop at their own pace, no-one is forced to perform and there are opportunities for you to explore performance techniques. Students will develop key skills in teamwork, communication and confidence whilst building friendships and having fun! The week ends with a showing, to friends and family, of the skills and musical numbers achieved during the course.</p>

  <div class="venue">
    <div class="venue__label">VENUE</div>
    The Village Hall<br>of St Aldric<br>Riverside<br>KT0 1AA
  </div>

  <div class="price">
    <div class="price__figure">30</div>per day
    <div class="price__divider"></div>
    <div class="price__figure">55</div>for both
  </div>

  <div class="workshop">
    <div class="workshop__brand"><span class="workshop__brand-dot"></span>Brightstep</div>
    <div class="workshop__details">WEST END WORKSHOP<br>Tuesday<br>5 &amp; 6 April 2016<br>8 – 16 years<br>1-4pm</div>
  </div>

  <div class="booking">
    <div class="booking__label">FOR BOOKING</div>
    <div class="booking__phone"><svg width="10" height="16" viewBox="0 0 10 16"><rect x="1" y="1" width="8" height="14" rx="1.5" fill="none" stroke="var(--blue)" stroke-width="1.6"/></svg>07700 900123</div>
    <div class="booking__email"><svg width="11" height="8" viewBox="0 0 11 8"><rect width="11" height="8" fill="var(--blue)"/><polyline points="0,0 5.5,4.5 11,0" fill="none" stroke="var(--white)" stroke-width="1"/></svg>brightstepdance@mail.com</div>
  </div>
</article>

</body>
</html>
```